Modern, corporate management consultancy firm needs a new website

We need a website for an Australian based management consultancy firm.

The company name is Corbel Strategy Partners.

We are looking for a parallax style wordpress site.

The site needs to provide the following functions:

1) subscribe function
2) links to social media (twitter, linkedin and mail)
3) a gated document section where people can download pdf's from the site after registering or providing name, company, position, email and contact number.

Attached is the company logo, would like to see designs that incorporate the dark blue and silver in the logo and separated into the following sections (Home, About, Services (with 4 options), Our Team, Links, Contacts.

Need the site to be easy to navigate and updated.

Potentially a News Section that can be updated regularly.

Target Market(s)

Target market is SME, business owners and directors

Industry/Entity Type

Management Consulting

Coding

Coded - Design and coding required

Number of Pages Required

1 page

Font styles to use
Sans Serif

Colors
0255a3
cbcbcb
757575
000000

Requirements
Must have
• Must be easy to read and use
Nice to have
• Features are listed on initial brief

```html
<!DOCTYPE html>
<html lang="en">
<head>
<meta charset="utf-8">
<title>Corbel Strategy Partners</title>
<link href="https://fonts.googleapis.com/css2?family=Roboto+Condensed:wght@300;400;700&family=Open+Sans:wght@400;600&display=swap" rel="stylesheet">
<style>
:root{
  --blue:#0255a3;
  --navy:#0f2d52;
  --silver:#cbcbcb;
  --grey:#757575;
  --black:#000000;
  --ink:#2c3440;
  --white:#ffffff;
  --slate:#1d2733;
  --footer:#1b2633;
}
*{margin:0;padding:0;box-sizing:border-box}
html,body{width:1200px;height:2800px;overflow:hidden}
body{font-family:"Open Sans",Arial,sans-serif;color:var(--ink);background:var(--white);position:relative}
.section{position:absolute;left:0;width:1200px;overflow:hidden}
.bg{position:absolute;inset:0}
.h-cond{font-family:"Roboto Condensed","Arial Narrow",sans-serif;font-weight:300}
.btn{display:inline-block;background:var(--navy);color:var(--white);font-size:14px;padding:10px 26px;border-radius:18px;text-decoration:none;border:1px solid rgba(255,255,255,.5)}

/* hero */
.hero{top:0;height:660px}
.hero .bg{background:linear-gradient(180deg,#3f8ed8 0%,#8cc3ee 38%,#d9e9f4 55%,#6d93b3 62%,#2e6391 80%,#1f4d78 100%)}
.nav{position:absolute;top:0;left:0;width:100%;height:48px;background:rgba(10,40,80,.45);display:flex;justify-content:center;gap:6px}
.nav a{color:var(--white);font-size:15px;text-decoration:none;padding:14px 26px;border-left:1px solid rgba(255,255,255,.35)}
.nav a:first-child{border-left:none;border-bottom:3px solid var(--white)}
.brand{position:absolute;top:130px;left:0;width:100%;display:flex;justify-content:center;align-items:center;gap:22px}
.brand-mark{width:110px;height:110px;border-radius:50%;background:var(--navy)}
.brand-name{font-family:"Open Sans",sans-serif;font-weight:600;font-size:40px;color:var(--navy)}
.hero-title{position:absolute;top:470px;width:100%;text-align:center;color:var(--white);font-size:72px;line-height:1.5;text-shadow:0 2px 6px rgba(0,0,0,.35)}

/* welcome */
.welcome{top:660px;height:412px;text-align:center}
.section-title{display:flex;align-items:center;justify-content:center;gap:22px;font-size:30px}
.section-title::before,.section-title::after{content:"";width:110px;height:1px;background:var(--silver)}
.welcome .section-title{margin-top:58px;color:var(--ink)}
.lead{font-size:14px;color:var(--grey);margin:14px auto 0;width:760px;line-height:1.6}
.welcome .btn{margin-top:20px}
.consultant-photo{position:absolute;left:500px;top:230px;width:200px;height:182px;border-radius:90px 90px 0 0;background:linear-gradient(180deg,#e4d3c4,#c7d3e0 60%,#f2f4f7)}

/* services */
.services{top:1072px;height:668px;color:var(--white);text-align:center}
.services .bg{background:linear-gradient(180deg,#243140 0%,#1a232e 55%,#2d3b4b 100%)}
.services .section-title{margin-top:44px;color:var(--white);position:relative}
.services .lead,.team .lead{color:#e6ecf2;width:700px}
.service-list{position:relative;display:flex;justify-content:center;gap:28px;margin-top:44px}
.service{width:240px}
.service-icon{width:124px;height:124px;border-radius:50%;border:3px solid rgba(255,255,255,.85);background:#10355f;margin:0 auto;display:flex;align-items:center;justify-content:center}
.service:nth-child(n+2) .service-icon{background:#141c25}
.service h3{font-family:"Roboto Condensed",sans-serif;font-weight:400;font-size:20px;margin-top:18px;line-height:1.25;min-height:50px}
.service p{font-size:13px;line-height:1.6;margin-top:10px;color:#d5dce4}
.services .btn{position:relative;margin-top:36px;background:transparent;border-color:var(--white)}

/* team */
.team{top:1760px;height:470px;color:var(--white)}
.team .bg{background:linear-gradient(180deg,#4c6585 0%,#7f93ad 45%,#5d7594 100%)}
.team .section-title{margin-top:34px;position:relative}
.team .lead{position:relative;text-align:center}
.member-photo{position:absolute;left:280px;top:150px;width:200px;height:200px;border-radius:50%;border:5px solid var(--white);background:linear-gradient(160deg,#e9e2dc,#b9c6d6)}
.member{position:absolute;left:520px;top:160px;width:420px}
.member h3{font-family:"Roboto Condensed",sans-serif;font-weight:400;font-size:22px}
.member p{font-size:17px;font-style:italic;line-height:1.5;margin-top:10px}
.social{display:flex;gap:10px;margin-top:22px}
.social span{width:32px;height:32px;background:var(--navy);display:block}
.dots{position:absolute;top:400px;left:560px;display:flex;gap:10px}
.dots span{width:10px;height:10px;border-radius:50%;background:rgba(255,255,255,.5)}
.dots span:first-child{background:var(--white)}

/* newsletter */
.newsletter{top:2230px;height:230px;text-align:center}
.newsletter .section-title{margin-top:34px;color:var(--ink)}
.newsletter .lead{margin-top:10px}
.subscribe{width:540px;height:50px;margin:28px auto 0;border:1px solid var(--silver);border-radius:25px;display:flex;align-items:center;justify-content:space-between;padding-left:22px}
.subscribe span{font-size:14px;color:var(--grey)}
.subscribe-go{width:50px;height:50px;border-radius:50%;background:var(--navy);display:flex;align-items:center;justify-content:center}

/* footer */
.footer{top:2460px;height:340px;color:var(--white);text-align:center}
.footer .bg{background:linear-gradient(180deg,#2d3a48 0%,#1b2633 60%,#121a23 100%)}
.footer h2{position:relative;font-family:"Roboto Condensed",sans-serif;font-weight:300;font-size:30px;margin-top:24px}
.contact-row{position:relative;display:flex;justify-content:space-between;width:1040px;margin:44px auto 0;font-size:14px;text-align:left}
.contact-row div{display:flex;align-items:flex-start;gap:12px;line-height:1.5}
.footer .social{position:relative;justify-content:center;margin-top:22px}
.footer .social span{background:transparent;border:1px solid var(--white)}
.copyright{position:relative;font-size:12px;color:var(--silver);margin-top:40px}
.to-top{position:relative;margin-top:18px}
</style>
</head>
<body>

<header class="section hero">
  <div class="bg" role="img" aria-label="Photograph of a harbour city skyline with opera house under blue sky"></div>
  <nav class="nav">
    <a href="#">Home</a><a href="#">About</a><a href="#">Services</a><a href="#">Our Team</a><a href="#">Links</a><a href="#">Contact</a>
  </nav>
  <div class="brand">
    <div class="brand-mark"></div>
    <div class="brand-name">Corbel Strategy Partners</div>
  </div>
  <h1 class="hero-title h-cond">Business Improvement<br>Specialists</h1>
</header>

<section class="section welcome">
  <h2 class="section-title h-cond">Welcome to Corbel Strategy Partners</h2>
  <p class="lead">Corbel Strategy Partners is a boutique management consulting firm that serves micro, small and mid-cap ASX listed and private companies.</p>
  <a class="btn" href="#">Learn More</a>
  <div class="consultant-photo" role="img" aria-label="Photograph of a smiling consultant wearing a headset"></div>
</section>

<section class="section services">
  <div class="bg" role="img" aria-label="Dark photograph of a business person touching a digital interface"></div>
  <h2 class="section-title h-cond">Our Services</h2>
  <p class="lead" style="position:relative">Lorem Ipsum is simply dummy text of the printing and typesetting industry. Lorem Ipsum has been the industry's standard dummy text ever since.</p>
  <div class="service-list">
    <div class="service">
      <div class="service-icon">
        <svg width="54" height="60" viewBox="0 0 54 60" fill="none" stroke="#fff" stroke-width="3"><path d="M27 6a16 16 0 0 0-9 29v7h18v-7a16 16 0 0 0-9-29z"/><path d="M19 48h16M21 54h12"/></svg>
      </div>
      <h3>Business Health<br>Check</h3>
      <p>Corbel Strategy Partners provides a fixed-fee health check for your business. We will meet with you and your key personnel.</p>
    </div>
    <div class="service">
      <div class="service-icon">
        <svg width="60" height="54" viewBox="0 0 60 54" fill="#fff"><rect x="22" y="2" width="16" height="12"/><rect x="2" y="38" width="16" height="12"/><rect x="22" y="38" width="16" height="12"/><rect x="42" y="38" width="16" height="12"/><path d="M29 14h2v10h20v14h-2V26H31v12h-2V26H11v12H9V24h20z"/></svg>
      </div>
      <h3>Business Performance<br>Consulting</h3>
      <p>Often times, we find that there are areas of a business which need attention, but business owners don't have the time to address.</p>
    </div>
    <div class="service">
      <div class="service-icon">
        <svg width="60" height="60" viewBox="0 0 60 60" fill="none" stroke="#fff" stroke-width="4"><circle cx="24" cy="32" r="12"/><circle cx="24" cy="32" r="4"/><circle cx="44" cy="16" r="8"/><path d="M24 14v6M24 44v6M6 32h6M36 32h6M44 4v4M44 24v4M32 16h4M52 16h4"/></svg>
      </div>
      <h3>Turnaround<br>Management</h3>
      <p>Turnaround management is a process that uses analysis and planning to identify the reasons for falling performance in the market.</p>
    </div>
    <div class="service">
      <div class="service-icon">
        <svg width="64" height="44" viewBox="0 0 64 44" fill="none" stroke="#fff" stroke-width="3" stroke-linejoin="round"><path d="M2 10l12-6 18 8 18-8 12 6M8 8l-4 18 20 14 6-4M56 8l4 18-16 12M20 20l10-6 14 12-4 4-10-8"/></svg>
      </div>
      <h3>Independent Insolvency<br>Advice</h3>
      <p>When a business encounters difficult financial circumstances, it can be a very stressful time for business owners and suppliers alike.</p>
    </div>
  </div>
  <a class="btn" href="#">Learn More</a>
</section>

<section class="section team">
  <div class="bg" role="img" aria-label="Soft blue photograph of a business professional"></div>
  <h2 class="section-title h-cond">Our Team</h2>
  <p class="lead">Lorem Ipsum is simply dummy text of the printing and typesetting industry. Lorem Ipsum has been the industry's standard dummy text ever since.</p>
  <div class="member-photo" role="img" aria-label="Portrait photograph of a team member"></div>
  <div class="member">
    <h3>Team Member Name</h3>
    <p>Lorem Ipsum is simply dummy text of the printing and typesetting industry. Lorem Ipsum has been the industry's standard dummy text ever since...</p>
    <div class="social"><span></span><span></span><span></span><span></span></div>
  </div>
  <div class="dots"><span></span><span></span><span></span><span></span></div>
</section>

<section class="section newsletter">
  <h2 class="section-title h-cond">Newsletter</h2>
  <p class="lead">Stay Connected! Sign up for our newsletter and get first pick off discounts and more!</p>
  <div class="subscribe">
    <span>Subscribe for Newsletter</span>
    <div class="subscribe-go"><svg width="20" height="16" viewBox="0 0 20 16" fill="none" stroke="#fff" stroke-width="2.5"><path d="M2 8h15M11 2l6 6-6 6"/></svg></div>
  </div>
</section>

<footer class="section footer">
  <div class="bg" role="img" aria-label="Dark photograph of a harbour with a bridge and opera house"></div>
  <h2>Corbel Strategy Partners</h2>
  <div class="contact-row">
    <div>
      <svg width="22" height="18" viewBox="0 0 22 18" fill="none" stroke="#fff" stroke-width="1.6"><rect x="1" y="1" width="20" height="14"/><path d="M6 17h10"/></svg>
      <span>Level 6, 120 Harbour Lane<br>Sydney NSW 2000 Australia</span>
    </div>
    <div>
      <svg width="22" height="16" viewBox="0 0 22 16" fill="none" stroke="#fff" stroke-width="1.6"><rect x="1" y="1" width="20" height="14"/><path d="M1 1l10 8 10-8"/></svg>
      <span>info@corbelstrategy.example</span>
    </div>
    <div>
      <svg width="18" height="18" viewBox="0 0 18 18" fill="#fff"><path d="M4 1l3 4-2 2a10 10 0 0 0 6 6l2-2 4 3-2 3C7 17 1 11 1 3z"/></svg>
      <span>+61 2 9000 0000</span>
    </div>
  </div>
  <div class="social"><span></span><span></span><span></span></div>
  <p class="copyright">© Corbel Strategy Partners 2015 - All rights reserved</p>
  <div class="to-top"><svg width="20" height="20" viewBox="0 0 20 20" fill="none" stroke="#fff" stroke-width="2.5"><path d="M3 10l7-7 7 7M3 17l7-7 7 7"/></svg></div>
</footer>

</body>
</html>
```